Nail Salon Business Card Design Project

We would like a business card design for a new nail salon using a logo supplied in eps format.

Depending on the success of this we will be creating projects for a price list, gift voucher and website design later also.

The business is called "Velvet Nail Salon". We provide manicure, spa pedicure and waxing services to professional ladies in the 30's age group.

The salon is very modern, clean, open and bright.

Target Market(s)

Ladies in their 30s.

Industry/Entity Type

Salon

Requirements
Must have
• On the front of the card we would like:
- the logo (see attached)
- address (Shop 14 Brindle Grove Shopping Centre
Tamworth Avenue
Canberra Airport ACT 2609)
- website address (www.velvetnails-example.com.au)
- email (kl@velvetnails-example.com.au)
- phone number (0418-574-203)

On the back we would like the trading hours, a grid/table (5 columns by 3 rows) for loyalty stamps, and an area for writing the customers next appointment. See attached for sample of content (card back.jpg).
Nice to have
• If possible it would be nice to have:
- a photo image
- facebook site address (http://www.facebook.com/velvetnailsalonexample)

I'm willing to pay extra (around $100) for the image if it can also be used on stationary and the website (projects for later).

```html
<!DOCTYPE html>
<html lang="en">
<head>
<meta charset="utf-8">
<title>Velvet Nail Salon – Business Card</title>
<link rel="stylesheet" href="https://fonts.googleapis.com/css2?family=Didact+Gothic&family=Source+Sans+3:wght@400;600&display=swap">
<style>
  :root {
    --backdrop: #ecebe8;
    --card: #ffffff;
    --pink: #e8529a;
    --pink-soft: #f3a9cb;
    --pink-faint: #fbe6f0;
    --grey: #939598;
    --ink: #3c3c3e;
    --line: #8a8a8c;
    --icon: #ffffff;
    --shadow: rgba(0, 0, 0, 0.18);
  }
  * { box-sizing: border-box; margin: 0; padding: 0; }
  html, body {
    width: 1200px;
    height: 975px;
    overflow: hidden;
    background: var(--backdrop);
  }
  .canvas { position: relative; width: 1200px; height: 975px; }

  .card {
    position: absolute;
    width: 640px;
    height: 380px;
    border-radius: 34px;
    background: var(--card);
    overflow: hidden;
    box-shadow: 0 6px 18px var(--shadow);
    font-family: "Source Sans 3", sans-serif;
    color: var(--ink);
  }
  .card-front { left: 70px; top: 50px; }
  .card-back { left: 490px; top: 510px; }

  .card-art { position: absolute; inset: 0; width: 100%; height: 100%; }

  .brand {
    position: absolute;
    font-family: "Didact Gothic", sans-serif;
    font-weight: 400;
    color: var(--pink);
    text-align: right;
    line-height: 1;
  }
  .brand-name { display: block; font-size: 54px; letter-spacing: 8px; }
  .brand-sub { display: block; font-size: 19px; letter-spacing: 3px; margin-top: 6px; }
  .card-front .brand { left: 70px; top: 95px; }
  .card-back .brand { left: 150px; top: 45px; }

  .staff {
    position: absolute;
    right: 40px;
    top: 222px;
    text-align: right;
  }
  .staff-name { font-size: 22px; font-weight: 600; color: var(--ink); margin-bottom: 8px; }
  .contact-line {
    display: flex;
    justify-content: flex-end;
    align-items: center;
    gap: 6px;
    font-size: 15px;
    line-height: 21px;
    color: var(--ink);
  }
  .contact-icon { width: 12px; height: 12px; flex: none; }

  .address {
    position: absolute;
    left: 60px;
    top: 268px;
    font-size: 14px;
    line-height: 19px;
    font-style: normal;
  }

  .hours {
    position: absolute;
    right: 44px;
    top: 40px;
    text-align: right;
    font-family: "Didact Gothic", sans-serif;
    font-size: 16px;
    line-height: 20px;
    color: var(--ink);
  }
  .section-title {
    font-family: "Didact Gothic", sans-serif;
    color: var(--pink);
    font-size: 16px;
    margin-bottom: 6px;
  }
  .hours .section-title { font-family: "Source Sans 3", sans-serif; font-weight: 600; font-size: 17px; }
  .hours-day + .hours-time { margin-bottom: 4px; }

  .loyalty { position: absolute; left: 58px; top: 200px; }
  .loyalty .section-title { text-align: center; }
  .stamp-grid {
    display: grid;
    grid-template-columns: repeat(5, 38px);
    grid-template-rows: repeat(3, 34px);
    border-top: 1px solid var(--line);
    border-left: 1px solid var(--line);
  }
  .stamp-grid span {
    border-right: 1px solid var(--line);
    border-bottom: 1px solid var(--line);
  }

  .appointment {
    position: absolute;
    left: 300px;
    top: 210px;
    width: 300px;
    font-family: "Didact Gothic", sans-serif;
    font-size: 15px;
    color: var(--ink);
  }
  .appointment-row { display: flex; align-items: baseline; margin-top: 10px; }
  .appointment-row .field { flex: 1; border-bottom: 1px dotted var(--ink); margin: 0 4px; }
  .appointment-row .field:last-child { margin-right: 0; }
</style>
</head>
<body>
<main class="canvas">

  <section class="card card-front" aria-label="Business card front">
    <svg class="card-art" viewBox="0 0 640 380">
      <defs>
        <linearGradient id="wave-pink" x1="0" y1="1" x2="1" y2="0">
          <stop offset="0" stop-color="#e8529a"/>
          <stop offset="1" stop-color="#f3a9cb"/>
        </linearGradient>
        <linearGradient id="portrait-tone" x1="0" y1="0" x2="0" y2="1">
          <stop offset="0" stop-color="#4a3a33"/>
          <stop offset="0.45" stop-color="#c99a80"/>
          <stop offset="1" stop-color="#5b4a45"/>
        </linearGradient>
        <radialGradient id="flourish-tone" cx="0.5" cy="0.5" r="0.5">
          <stop offset="0" stop-color="#fbe6f0"/>
          <stop offset="1" stop-color="#ffffff" stop-opacity="0"/>
        </radialGradient>
      </defs>
      <ellipse role="img" aria-label="Faint floral flourish decoration" cx="290" cy="220" rx="150" ry="120" fill="url(#flourish-tone)"/>
      <path role="img" aria-label="Portrait photo of salon staff member" d="M360 40 H540 C565 75 575 125 562 176 C520 215 470 250 420 280 H360 Z" fill="url(#portrait-tone)"/>
      <path class="band-grey" d="M525 0 H640 V92 C615 125 590 155 562 176 C578 112 566 50 525 0 Z" fill="#939598"/>
      <path class="band-pink" d="M170 380 C360 335 545 230 640 88 V380 Z" fill="url(#wave-pink)"/>
    </svg>

    <div class="brand">
      <span class="brand-name">Velvet</span>
      <span class="brand-sub">Nail Salon</span>
    </div>

    <div class="staff">
      <p class="staff-name">Name Here</p>
      <p class="contact-line">0418-574-203
        <svg class="contact-icon" viewBox="0 0 12 12"><rect x="3" y="0.5" width="6" height="11" rx="1.2" fill="var(--icon)"/><rect x="4" y="2" width="4" height="6" fill="#e8529a"/><circle cx="6" cy="9.7" r="0.8" fill="#e8529a"/></svg>
      </p>
      <p class="contact-line">kl@velvetnails-example.com.au
        <svg class="contact-icon" viewBox="0 0 12 12"><rect x="0.8" y="2.3" width="10.4" height="7.4" fill="var(--icon)"/><path d="M1 2.6 L6 6.6 L11 2.6" fill="none" stroke="#e8529a" stroke-width="1"/></svg>
      </p>
      <p class="contact-line">www.velvetnails-example.com.au
        <svg class="contact-icon" viewBox="0 0 12 12"><circle cx="6" cy="6" r="5.2" fill="var(--icon)"/><circle cx="6" cy="6" r="3.6" fill="none" stroke="#e8529a" stroke-width="0.9"/><path d="M2.4 6 H9.6 M6 2.4 V9.6" stroke="#e8529a" stroke-width="0.9"/></svg>
      </p>
    </div>

    <address class="address">
      Shop 14 Brindle Grove Shopping Centre<br>
      Tamworth Avenue<br>
      Canberra Airport ACT 2609
    </address>
  </section>

  <section class="card card-back" aria-label="Business card back">
    <div class="brand">
      <span class="brand-name">Velvet</span>
      <span class="brand-sub">Nail Salon</span>
    </div>

    <div class="hours">
      <p class="section-title">Trading Hours</p>
      <p class="hours-day">Monday to Friday</p>
      <p class="hours-time">9.30am to 5.30pm</p>
      <p class="hours-day">Saturday</p>
      <p class="hours-time">9.30am to 1pm</p>
    </div>

    <div class="loyalty">
      <p class="section-title">loyalty stamps</p>
      <div class="stamp-grid" role="table" aria-label="Loyalty stamp grid">
        <span></span><span></span><span></span><span></span><span></span>
        <span></span><span></span><span></span><span></span><span></span>
        <span></span><span></span><span></span><span></span><span></span>
      </div>
    </div>

    <div class="appointment">
      <p class="section-title">Appointment</p>
      <p class="appointment-row">Date<span class="field"></span>Day<span class="field"></span>Time<span class="field"></span></p>
      <p class="appointment-row">Date<span class="field"></span>Day<span class="field"></span>Time<span class="field"></span></p>
      <p class="appointment-row">Date<span class="field"></span>Day<span class="field"></span>Time<span class="field"></span></p>
    </div>
  </section>

</main>
</body>
</html>
```